Poem Handwritten by Veteran while in the jungle of Vietnam

My parents are celebrating their 50th wedding anniversary this year. I wanted to give them a very memorable gift. On my parents 2nd anniversary, my father was stationed in Vietnam. On that night he was in the jungle waiting till morning and wrote a poem to my mother using his pant leg as paper. I would like this poem to typographically designed to be framed and hung on the wall.

I have attached a picture of the poem below. It will need to be 11x14 when printed for framing. It would be great if there was background or artwork to make it more visually interesting, perhaps in a watercolor. My parents have a transitional style. I have attached some possible color schemes as well. Cool greens, blue, neutral grays, with hints of berries or highlights of yellow. These are just a guide, I would be open to your interpretations.

Thank you for your help. This will hopefully be a gift they will truly treasure as much as the poem itself.

Target Market(s)

My parents who are excited to be celebrating their 50th wedding anniversary. It should have a transitional, mature style.

Font styles to use
Serif
Script

Requirements
Must have
• The poem, typographically designed. There can be a mix of fonts, but legibility is critically important.
• Now that some designs have come through I wanted to give some more guidance of what I'm looking for. I want something that feels sophisticated and artistic.
Nice to have
• A background or art work, using the color schemes attached as a guide. I am really liking the designs that have a full color landscape artwork in the background. The fonts should be elegant and formal. I really like the romantic, muted colors. I had trouble finding similar projects online in the style I wanted until I cam across wedding invites. Those seem to be the most applicable. I've added pictures of some so you can get a sense of what I'm looking for. I am really liking the jungle foliage, starry skies or sunrises.
Should not have
• Cartoon caricatures, fonts that are too illegible when printed. I'm not liking anything whimsical. I don't like the very bright colors for this project.

```html
<!DOCTYPE html>
<html lang="en">
<head>
<meta charset="utf-8">
<title>Walter's Anniversary Poem</title>
<link rel="stylesheet" href="https://fonts.googleapis.com/css2?family=Abril+Fatface&family=Allura&family=Libre+Baskerville:wght@400&display=swap">
<style>
  :root {
    --page: #ececec;
    --paper: #f6f7f4;
    --ink: #2f2f2f;
    --ink-soft: #444;
    --plum: #5b1e3c;
    --plum-deep: #3e1b4a;
    --violet: #9a5ad6;
    --blue: #5a5fd0;
    --teal: #3d9a8a;
    --leaf: #8fbf6a;
    --berry: #d25ab8;
    --sun: #e6d23a;
    --canvas-olive: #7d8466;
    --canvas-dark: #6a7258;
  }
  * { margin: 0; padding: 0; box-sizing: border-box; }
  html, body { width: 1200px; height: 1200px; overflow: hidden; background: var(--page); }
  .poster {
    position: absolute; left: 217px; top: 27px;
    width: 765px; height: 1145px; overflow: hidden;
    background: var(--paper);
  }
  .poster-art {
    position: absolute; inset: 0;
    background:
      radial-gradient(ellipse 180px 140px at 95% 25%, rgba(230,210,58,.55), transparent 70%),
      radial-gradient(ellipse 260px 220px at 5% 5%, rgba(90,95,208,.75), transparent 70%),
      radial-gradient(ellipse 280px 260px at 92% 10%, rgba(154,90,214,.75), transparent 70%),
      radial-gradient(ellipse 220px 200px at 20% 22%, rgba(210,90,184,.55), transparent 70%),
      radial-gradient(ellipse 140px 300px at 0% 40%, rgba(61,154,138,.55), transparent 70%),
      radial-gradient(ellipse 160px 260px at 100% 55%, rgba(143,191,106,.45), transparent 70%),
      radial-gradient(ellipse 200px 120px at 55% 8%, rgba(120,110,220,.35), transparent 70%),
      linear-gradient(to bottom, transparent 0%, transparent 68%, rgba(125,132,102,.55) 78%, var(--canvas-olive) 90%, var(--canvas-dark) 100%);
  }
  .poster-content { position: absolute; inset: 0; text-align: center; }
  .intro {
    position: absolute; top: 160px; left: 125px; width: 525px;
    font: 11px/15px "Libre Baskerville", serif; color: var(--ink-soft);
  }
  .dateline {
    position: absolute; top: 252px; left: 0; right: 0;
    font: 21px/1 "Abril Fatface", serif; color: var(--plum-deep); letter-spacing: .3px;
  }
  .title-name {
    position: absolute; top: 305px; left: 0; right: 0;
    font: 50px/1 "Abril Fatface", serif; color: var(--plum); letter-spacing: 1px;
  }
  .title-script {
    position: absolute; top: 338px; left: 0; right: 0;
    font: 92px/1 "Allura", cursive; color: var(--plum);
  }
  .poem {
    position: absolute; top: 462px; width: 340px;
    font: 13.5px/18.3px "Libre Baskerville", serif; color: var(--ink);
  }
  .poem-left { left: 66px; }
  .poem-right { left: 390px; }
  .stanza { margin-bottom: 18.3px; }
</style>
</head>
<body>
<div class="poster">
  <div class="poster-art" role="img" aria-label="Watercolour jungle foliage in violet, blue, teal and green with yellow highlights, fading into a faded olive uniform fabric bearing a pencilled line of the poem"></div>
  <div class="poster-content">
    <p class="intro">This poem was written during the dark of night while on guard duty at LZ Professional in Viet Nam. I was at the time a 2nd Lieutenant in the Infantry. The date was July, 1970, our second anniversary. The original was penciled onto my army uniform, arranging only the key rhyming words without light to see</p>
    <p class="dateline">20 July 1970, Monday, LZ Professional</p>
    <h1 class="title-name">Walter's</h1>
    <h2 class="title-script">Anniversary Poem</h2>

    <div class="poem poem-left">
      <p class="stanza">Life's journey began with a challenge,<br>It was heralded far and near.<br>The road led on forever,<br>Its completion was known to be dear.</p>
      <p class="stanza">From the garden of light it proceeded,<br>To the valley of shadows it led.<br>Thorns and thistles adorned it,<br>Past abyss and crevice it sped.</p>
      <p class="stanza">The brave surged forward with courage,<br>The wise undaunted pressed on.<br>The mighty held high their banner,<br>We all awaited the dawn.</p>
      <p class="stanza">Though the pitfalls and hazards were many,<br>The pathway was clearly in view.<br>Straight and sure it glided,<br>Its course we knew to be true.</p>
      <p class="stanza">I knew you, Sweetheart, beforehand,<br>So precious and sweet were you.<br>Our moments of bliss were priceless,<br>Each day brought us joy anew.</p>
      <p class="stanza">The call to progression beckoned,<br>At last I would have my chance –<br>To clasp you to me forever,<br>And seal our divine romance.</p>
    </div>

    <div class="poem poem-right">
      <p class="stanza">I eagerly started the journey,<br>Though with sorrow, I left you behind.<br>With courage and faith I continued,<br>For I knew, that you later I'd find.</p>
      <p class="stanza">I diligently searched for you, Darling,<br>The roadway was both bleak and fair.<br>Though the years grew long in number,<br>I did not give up in despair.</p>
      <p class="stanza">At last in the distance I saw you,<br>So beautiful, lovely, and sweet!<br>Your attention I struggled to capture,<br>Your love I wrested to meet.</p>
      <p class="stanza">What rapture was mine in fulfillment,<br>As now together we stand.<br>To cherish and love each other,<br>While our plans and dreams expand.</p>
      <p class="stanza">I love you, Darling, forever,<br>My life you have made replete.<br>Our eternal mansion beckons<br>Your love has made it complete.</p>
    </div>
  </div>
</div>
</body>
</html>
```